Business card design needed

I need a business card for my private practice. I would like to see the designs that use bright blue and white. I would like to see similar designs as to the card below:
http://blog.printmoss.com/2009/designing-a-business-card-with-pm-kt517-template.html
I would like to see the back of the card have room for appointment times. Thank you.

Industry/Entity Type
Business
Contact Information for Business Card
Tandem Wellbeing & Guidance Services
Fiona Marsh B.Psychology
Registered Psychologist
Building C, Level 3, 14 Wattle Crescent, Canberra, ACT 2601
T: (02) 6248 7315
F: (02) 6248 7390
info@tandemwellbeing.com.au
www.tandemwellbeing.com.au

```html
<!DOCTYPE html>
<html lang="en">
<head>
<meta charset="utf-8">
<title>Tandem Wellbeing &amp; Guidance Services – Business Card</title>
<link rel="stylesheet" href="https://fonts.googleapis.com/css2?family=Marcellus+SC&family=Cabin:wght@400;500&display=swap">
<style>
  :root {
    --brand-blue: #1c2a8c;
    --card-white: #ffffff;
    --ink: #1a1a1a;
    --stage: #2a2a2a;
  }
  * { margin: 0; padding: 0; box-sizing: border-box; }
  html, body {
    width: 1200px; height: 900px; overflow: hidden;
    background: var(--stage);
  }
  .canvas {
    position: relative; width: 1200px; height: 900px;
  }
  .card {
    position: absolute; left: 250px; width: 700px; height: 400px;
    overflow: hidden;
  }
  .card-front { top: 40px; background: var(--brand-blue); }
  .card-back { top: 460px; background: var(--card-white); }
  .card-shape { position: absolute; inset: 0; width: 100%; height: 100%; }

  .business-name {
    position: absolute; right: 60px; top: 120px;
    font-family: "Marcellus SC", serif;
    font-size: 34px; line-height: 1.2; color: var(--card-white);
    text-align: right; letter-spacing: 0.5px;
  }

  .contact-block {
    position: absolute; right: 56px; top: 50px;
    font-family: "Cabin", sans-serif; color: var(--ink);
    text-align: right; font-size: 17px; line-height: 1.3;
  }
  .person-name { font-size: 30px; font-weight: 500; color: var(--brand-blue); line-height: 1.1; }
  .credentials { margin-bottom: 44px; }
  .address { margin-bottom: 18px; }
  .phone-lines { margin-bottom: 24px; }
  .label { color: var(--brand-blue); }
</style>
</head>
<body>
<main class="canvas">
  <section class="card card-front" aria-label="Card front">
    <svg class="card-shape" viewBox="0 0 700 400" aria-hidden="true">
      <circle cx="-10" cy="330" r="250" fill="var(--card-white)"/>
    </svg>
    <h1 class="business-name">Tandem Wellbeing<br>&amp; Guidance Services</h1>
  </section>

  <section class="card card-back" aria-label="Card back">
    <svg class="card-shape" viewBox="0 0 700 400" aria-hidden="true">
      <circle cx="120" cy="440" r="270" fill="var(--brand-blue)"/>
    </svg>
    <div class="contact-block">
      <p class="person-name">Fiona Marsh</p>
      <p class="credentials">B.Psychology<br>Registered Psychologist</p>
      <p class="address">Building C, Level 3, 14 Wattle Crescent<br>Canberra, ACT 2601</p>
      <p class="phone-lines"><span class="label">T:</span> (02) 6248 7315<br><span class="label">F:</span> (02) 6248 7390</p>
      <p class="web-lines">info@tandemwellbeing.com.au<br>www.tandemwellbeing.com.au</p>
    </div>
  </section>
</main>
</body>
</html>
```